Delia Morvan
exclusive handcrafted jewelry
Simple
delmorvan@quillbox.net
deliamorvandesign.net
business card should be shaded black like uploaded logo.
I also like the royal blue option !
I have no idea what is on that file since I can not open it . I hope it is my logo in blue or shaded black.

```html
<!DOCTYPE html>
<html lang="en">
<head>
<meta charset="utf-8">
<title>Delia Morvan – Business Card</title>
<link rel="stylesheet" href="https://fonts.googleapis.com/css2?family=Josefin+Sans:ital,wght@0,300;0,400;1,300&display=swap">
<style>
  :root {
    --page: #ffffff;
    --card-dark: #17171c;
    --card-edge: #0e0e12;
    --glow: #3b3190;
    --glow-deep: #24205a;
    --ink-light: #f2f2f6;
    --ink-soft: #b9b9c6;
    --ink-muted: #8e8ea4;
    --mark: #6b66b8;
  }
  * { margin: 0; padding: 0; box-sizing: border-box; }
  html, body {
    width: 1200px; height: 686px; overflow: hidden;
    background: var(--page);
  }
  .card {
    position: relative;
    width: 1200px; height: 686px;
    border-radius: 28px;
    overflow: hidden;
    background:
      radial-gradient(ellipse 380px 300px at 600px 330px, var(--glow) 0%, var(--glow-deep) 45%, rgba(23,23,28,0) 100%),
      repeating-linear-gradient(90deg, rgba(255,255,255,0.025) 0 2px, rgba(0,0,0,0) 2px 9px),
      linear-gradient(180deg, var(--card-dark), var(--card-edge));
    font-family: "Josefin Sans", sans-serif;
  }
  .card__owner {
    position: absolute;
    top: 98px; right: 104px;
    font-size: 40px; font-weight: 300;
    color: var(--ink-light);
    letter-spacing: 0.5px;
  }
  .brand {
    position: absolute;
    left: 0; right: 0; top: 240px;
    text-align: center;
  }
  .brand__dot {
    display: block;
    width: 96px; height: 96px;
    margin: 0 auto 28px;
    border-radius: 50%;
    background: var(--mark);
  }
  .brand__name {
    font-size: 60px; font-weight: 300;
    color: var(--ink-light);
    letter-spacing: 6px;
    line-height: 1;
  }
  .brand__tagline {
    margin-top: 10px;
    font-size: 19px; font-weight: 400;
    color: var(--ink-soft);
    letter-spacing: 2px;
    text-transform: uppercase;
  }
  .contact {
    position: absolute;
    left: 0; right: 0; top: 505px;
    text-align: center;
    list-style: none;
    font-size: 26px; font-weight: 300; font-style: italic;
    color: var(--ink-muted);
    line-height: 37px;
    letter-spacing: 1px;
  }
  .card__corner {
    position: absolute;
    right: 60px; bottom: 44px;
    font-size: 26px; font-weight: 300;
    color: var(--mark);
  }
</style>
</head>
<body>
  <div class="card">
    <div class="card__owner">Delia Morvan</div>

    <div class="brand">
      <span class="brand__dot"></span>
      <div class="brand__name">Delia Morvan</div>
      <div class="brand__tagline">Exclusive Handcrafted Jewelry</div>
    </div>

    <ul class="contact">
      <li>Phone : 305-555-0142</li>
      <li>Email : delmorvan@quillbox.net</li>
      <li>web: deliamorvandesign.net</li>
    </ul>

    <div class="card__corner">Delia Morvan</div>
  </div>
</body>
</html>
```